Construction business card

I need a new business card, they can connect with my logo, brand.
What we do is residential house , design and build
I like: Navy blue / black
I attached our logo, brand,
and, some idea for business card.

```html
<!DOCTYPE html>
<html lang="en">
<head>
<meta charset="utf-8">
<title>Ridgeline Homes – Business Cards</title>
<link rel="stylesheet" href="https://fonts.googleapis.com/css2?family=Jost:wght@400;500;600&display=swap">
<style>
  :root {
    --page-bg: #3a3a3a;
    --card-bg: #1c1d21;
    --card-bg-back: #222326;
    --ink-white: #ffffff;
    --ink-soft: #e6e6e6;
    --brand-blue: #3b86c6;
    --strip-dark: #0d1110;
    --deco-dark: #0b0b0c;
    --deco-mid: #3c3c3f;
  }
  * { margin: 0; padding: 0; box-sizing: border-box; }
  html, body {
    width: 1200px; height: 900px; overflow: hidden;
    background: var(--page-bg);
    font-family: "Jost", "Futura", sans-serif;
  }
  .sheet { position: relative; width: 1200px; height: 900px; }
  .card {
    position: absolute; width: 514px; height: 296px;
    background: var(--card-bg);
    box-shadow: 0 8px 18px rgba(0,0,0,.45);
    overflow: hidden;
  }
  .card--front-a { left: 73px;  top: 138px; }
  .card--front-b { left: 73px;  top: 464px; }
  .card--back-a  { left: 614px; top: 138px; background: var(--card-bg-back); }
  .card--back-b  { left: 614px; top: 464px; background: var(--card-bg-back); }

  .brand {
    position: absolute; inset: 0;
    display: flex; align-items: center; justify-content: center; gap: 14px;
  }
  .brand__mark { width: 22px; height: 22px; background: var(--brand-blue); }
  .brand__name {
    color: var(--ink-white); font-weight: 600; font-size: 34px;
    letter-spacing: 2px; text-transform: uppercase;
  }

  .holder { position: absolute; left: 40px; top: 34px; color: var(--ink-white); }
  .holder__name { font-size: 20px; font-weight: 500; line-height: 1.1; }
  .holder__role { font-size: 14px; font-weight: 400; line-height: 1.2; }

  .contact {
    position: absolute; right: 38px; top: 38px; text-align: right;
    color: var(--ink-soft); font-size: 12px; line-height: 16px;
  }

  .decor {
    position: absolute; left: 0; top: 92px; width: 514px; height: 172px;
    background: linear-gradient(110deg, var(--deco-dark) 0%, #1a1a1c 45%, var(--deco-mid) 75%, #2a2a2c 100%);
  }
  .footer-band { position: absolute; left: 0; top: 0; width: 514px; height: 296px; }
  .address {
    position: absolute; right: 36px; bottom: 7px;
    color: var(--ink-white); font-size: 17px; font-weight: 400;
  }
</style>
</head>
<body>
<main class="sheet">

  <section class="card card--front-a">
    <div class="brand">
      <span class="brand__mark"></span>
      <span class="brand__name">Ridgeline Homes</span>
    </div>
  </section>

  <section class="card card--front-b">
    <div class="brand">
      <span class="brand__mark"></span>
      <span class="brand__name">Ridgeline Homes</span>
    </div>
  </section>

  <section class="card card--back-a">
    <div class="holder">
      <p class="holder__name">Daniel Marsh</p>
      <p class="holder__role">managing director</p>
    </div>
    <div class="contact">
      <p>0400 555 018</p>
      <p>daniel@ridgelinehomes.com.au</p>
      <p>ridgelinehomes.com.au</p>
    </div>
    <div class="decor" role="img" aria-label="Large dark glossy roofline brand graphic"></div>
    <svg class="footer-band" viewBox="0 0 514 296" aria-hidden="true">
      <polygon points="155,264 514,264 514,296 112,296" fill="#0d1110"/>
      <polygon points="100,296 148,258 514,258 514,264 155,264 112,296" fill="#ffffff"/>
    </svg>
    <p class="address">42 Harrow St., Elmwood, Vic 3190</p>
  </section>

  <section class="card card--back-b">
    <div class="holder">
      <p class="holder__name">Daniel Marsh</p>
      <p class="holder__role">managing director</p>
    </div>
    <div class="contact">
      <p>0400 555 018</p>
      <p>daniel@ridgelinehomes.com.au</p>
      <p>ridgelinehomes.com.au</p>
    </div>
    <div class="decor" role="img" aria-label="Large dark glossy roofline brand graphic"></div>
    <svg class="footer-band" viewBox="0 0 514 296" aria-hidden="true">
      <polygon points="155,264 514,264 514,296 112,296" fill="#0d1110"/>
      <polygon points="100,296 148,258 514,258 514,264 155,264 112,296" fill="#ffffff"/>
    </svg>
    <p class="address">42 Harrow St., Elmwood, Vic 3190</p>
  </section>

</main>
</body>
</html>
```